Vellorin - Business Cards for a new venture

create business card for a startup classified business dealing in construction materials, the cards need to have a professional look but modern, more serious than playful, one of the samples must include the official font (attached), please explore using the official colors in the company's logo

Target Market(s)

Energy sector

Contact Information for Business Card

Font styles to use
Other font styles liked:
• suissnord

Requirements
Must have
• corporate colors (in logo attached)
Nice to have
• Official font (in one of the samples) font is : suissnord
Should not have
• Cartoonish look

```html
<!DOCTYPE html>
<html lang="en">
<head>
<meta charset="utf-8">
<title>Vellorin Business Cards</title>
<link rel="stylesheet" href="https://fonts.googleapis.com/css2?family=Raleway:wght@400;500;700&display=swap">
<style>
  :root {
    --navy: #0b4577;
    --navy-dark: #0a2f5a;
    --grey: #9a9ea3;
    --grey-line: #c4c7ca;
    --grey-text: #6f7378;
    --paper: #ffffff;
    --backdrop: #e9e6e3;
  }
  html, body {
    margin: 0;
    width: 1200px;
    height: 997px;
    overflow: hidden;
    background: var(--backdrop);
    font-family: "Raleway", sans-serif;
  }
  .sheet {
    position: relative;
    width: 1200px;
    height: 997px;
  }
  .card {
    position: absolute;
    top: 350px;
    width: 520px;
    height: 297px;
    box-shadow: 0 6px 18px rgba(0,0,0,0.12);
    overflow: hidden;
  }
  .card-front { left: 50px; background: var(--paper); }
  .card-back { left: 630px; background: var(--navy); }

  .front-art { position: absolute; inset: 0; }

  .brand-mark {
    position: absolute;
    left: 48px;
    top: 62px;
    display: flex;
    align-items: center;
    gap: 12px;
    color: var(--grey);
    font-weight: 500;
    font-size: 28px;
    letter-spacing: 4px;
    text-transform: uppercase;
  }
  .brand-mark .dot {
    width: 13px; height: 13px;
    border-radius: 50%;
    background: var(--navy);
  }

  .holder {
    position: absolute;
    right: 26px;
    top: 30px;
    text-align: right;
  }
  .holder-name {
    color: var(--navy-dark);
    font-weight: 700;
    font-size: 17px;
  }
  .holder-title {
    color: var(--grey-text);
    font-size: 12px;
    margin-top: 3px;
  }

  .address {
    position: absolute;
    right: 26px;
    top: 86px;
    text-align: right;
    color: var(--grey-text);
    font-size: 12px;
    line-height: 17px;
  }
  .website {
    position: absolute;
    right: 26px;
    top: 131px;
    color: #fff;
    font-size: 12px;
    line-height: 15px;
    letter-spacing: 0.3px;
  }

  .contacts {
    position: absolute;
    left: 36px;
    top: 170px;
    margin: 0; padding: 0;
    list-style: none;
    color: var(--grey-text);
    font-size: 12.5px;
  }
  .contacts li {
    display: flex;
    align-items: center;
    gap: 9px;
    height: 18px;
  }
  .contacts svg { width: 11px; height: 11px; fill: var(--navy); }

  .back-brand {
    position: absolute;
    left: 0; right: 0;
    top: 130px;
    text-align: center;
    color: #fff;
    font-weight: 500;
    font-size: 34px;
    letter-spacing: 6px;
    text-transform: uppercase;
  }
</style>
</head>
<body>
<main class="sheet">

  <section class="card card-front" aria-label="Business card front">
    <svg class="front-art" viewBox="0 0 520 297" aria-hidden="true">
      <line x1="40" y1="154" x2="250" y2="154" stroke="var(--grey-line)" stroke-width="1"/>
      <path d="M240 152 C300 152 310 128 380 128 L520 128 L520 150 L390 150 C330 150 310 156 240 156 Z" fill="var(--navy)"/>
      <path d="M40 240 L290 240 C350 240 360 154 430 154 L520 154 L520 161 L430 161 C370 161 360 247 290 247 L40 247 Z" fill="var(--grey)"/>
    </svg>

    <div class="brand-mark"><span class="dot"></span>Vellorin</div>

    <div class="holder">
      <div class="holder-name">Dana Whitfield</div>
      <div class="holder-title">President</div>
    </div>

    <div class="address">Po. box 201, Street Name,<br>City Name, Zip Code - 00000</div>
    <div class="website">www.vellorin.com</div>

    <ul class="contacts">
      <li><svg viewBox="0 0 12 12"><path d="M1 3 Q6 0 11 3 L10 5 L8 4 L8 3 Q6 2 4 3 L4 4 L2 5 Z M3 6 H9 V11 H3 Z"/></svg>(555) 014-2287</li>
      <li><svg viewBox="0 0 12 12"><path d="M3.5 0 H8.5 V12 H3.5 Z M4.5 1.5 V8.5 H7.5 V1.5 Z"/></svg>(555) 014-2288</li>
      <li><svg viewBox="0 0 12 12"><path d="M0 2 H12 V10 H0 Z M1 3 L6 7 L11 3 Z" fill-rule="evenodd"/></svg>info@vellorin.com</li>
    </ul>
  </section>

  <section class="card card-back" aria-label="Business card back">
    <div class="back-brand">Vellorin</div>
  </section>

</main>
</body>
</html>
```